Baby prediction and advice cards, thank you notes, Baby shower invitations and diaper raffle tickets

Please see attached brief with description of the project.

*** Only apply if you are DETAIL ORIENTED and willing to read 100% the brief and the correction instructions (if required)***

*** Only apply if you are able to communicate in English 100%***

We need QUALITY over quantity

Contact us if you have questions.

Thank you

Target Market(s)

Expecting mothers and their families (Mothers, sisters)

Font styles to use
Sans Serif

Colors

Designer to choose colors to be used in the design.

Requirements
Must have
• Read the brief
Should not have
• Read the brief

```html
<!DOCTYPE html>
<html lang="en">
<head>
<meta charset="utf-8">
<title>Baby Shower Stationery Set</title>
<link href="https://fonts.googleapis.com/css2?family=Pacifico&family=Fira+Sans:wght@400&family=Varela+Round&display=swap" rel="stylesheet">
<style>
  :root {
    --kraft: #e6cb9f;
    --ink: #3b3733;
    --ink-soft: #4a4540;
    --rule: #5a534b;
    --ribbon-pink: #f7cdbc;
    --ribbon-blue: #cde2e6;
    --glow: #f6e7b6;
    --page: #ffffff;
  }
  * { margin: 0; padding: 0; box-sizing: border-box; }
  html, body { width: 1200px; height: 978px; overflow: hidden; background: var(--page); }
  body { position: relative; font-family: "Fira Sans", sans-serif; color: var(--ink); }
  .card { position: absolute; background: var(--kraft); overflow: hidden; }
  .abs { position: absolute; white-space: nowrap; line-height: 1; }
  .script { font-family: "Pacifico", cursive; color: var(--ink); text-shadow: 1.5px 1.5px 0 var(--glow); }
  .label { font-size: 13px; color: var(--ink-soft); }
  .rule { position: absolute; height: 0; border-top: 1px solid var(--rule); }
  .dots { position: absolute; height: 0; border-top: 2px dotted var(--ink-soft); }
  .box { display: inline-block; width: 13px; height: 13px; border: 1.5px solid var(--ink-soft); border-radius: 3px; vertical-align: -2px; margin-right: 5px; }
  .caption { position: absolute; font-family: "Varela Round", sans-serif; font-size: 21px; color: #111; transform: translateX(-50%); white-space: nowrap; }
  .center { transform: translateX(-50%); text-align: center; }
</style>
</head>
<body>

<!-- Predictions & advice card, front -->
<section class="card predictions-front" style="left:0;top:0;width:525px;height:374px;">
  <svg class="title-ribbon" style="position:absolute;left:52px;top:35px" width="422" height="43" viewBox="0 0 422 43">
    <polygon points="0,0 252,0 252,43 0,43 22,21.5" fill="var(--ribbon-pink)"/>
    <polygon points="252,0 422,0 400,21.5 422,43 252,43" fill="var(--ribbon-blue)"/>
    <polyline points="4,3 418,3" stroke="#8a8a8a" stroke-width="1" stroke-dasharray="3 2" fill="none"/>
    <polyline points="4,40 418,40" stroke="#8a8a8a" stroke-width="1" stroke-dasharray="3 2" fill="none"/>
  </svg>
  <div class="abs script" style="left:106px;top:40px;font-size:25px;">Baby Predictions</div>
  <div class="abs script" style="left:300px;top:30px;font-size:36px;">&amp;</div>
  <div class="abs script" style="left:350px;top:40px;font-size:25px;">Advice</div>

  <div class="abs label" style="left:21px;top:100px;">Baby’s name:</div>
  <div class="rule" style="left:110px;width:180px;top:113px;"></div>
  <div class="abs label" style="left:21px;top:130px;">Gender: &nbsp; <span class="box"></span>Boy &nbsp;&nbsp; <span class="box"></span>Girl</div>
  <div class="abs label" style="left:21px;top:159px;">Date of birth:</div>
  <div class="rule" style="left:110px;width:180px;top:172px;"></div>
  <div class="abs label" style="left:21px;top:187px;">Time of birth:</div>
  <div class="rule" style="left:112px;width:178px;top:201px;"></div>
  <div class="abs label" style="left:21px;top:217px;">Weight:</div>
  <div class="rule" style="left:76px;width:77px;top:230px;"></div>
  <div class="abs label" style="left:163px;top:217px;">Length:</div>
  <div class="rule" style="left:216px;width:74px;top:230px;"></div>
  <div class="abs label" style="left:21px;top:246px;">Hair color:</div>
  <div class="rule" style="left:93px;width:60px;top:259px;"></div>
  <div class="abs label" style="left:163px;top:246px;">Eye color:</div>
  <div class="rule" style="left:231px;width:59px;top:259px;"></div>

  <div style="position:absolute;left:302px;top:94px;height:172px;border-left:2px dotted var(--ink-soft);"></div>

  <div class="abs label" style="left:314px;top:100px;">Resemblance: &nbsp;&nbsp;&nbsp;</div>
  <div class="abs label" style="left:420px;top:100px;"><span class="box"></span>Both</div>
  <div class="abs label" style="left:337px;top:130px;"><span class="box"></span>All dad</div>
  <div class="abs label" style="left:420px;top:130px;"><span class="box"></span>All mom</div>
  <div class="abs label" style="left:314px;top:159px;">I hope you get mom’s:</div>
  <div class="rule" style="left:314px;width:190px;top:201px;"></div>
  <div class="abs label" style="left:314px;top:217px;">I hope you get dad’s:</div>
  <div class="rule" style="left:314px;width:190px;top:259px;"></div>

  <div class="abs label" style="left:21px;top:288px;">My best advice:</div>
  <div class="rule" style="left:125px;width:379px;top:299px;"></div>
  <div class="abs script" style="left:45px;top:316px;font-size:17px;">Best wishes and love from:</div>
  <div class="rule" style="left:258px;width:222px;top:339px;"></div>
</section>

<!-- Predictions & advice card, back -->
<section class="card predictions-back" style="left:0;top:388px;width:525px;height:374px;" role="img" aria-label="Card back with a soft pastel confetti pattern of circles, squares and triangles"></section>
<div class="caption" style="left:262px;top:780px;">Baby predictions and advice game</div>

<!-- Thank you card -->
<section class="card thanks-front" style="left:550px;top:0;width:319px;height:412px;" role="img" aria-label="Card front with pastel confetti pattern">
  <div class="abs script center" style="left:160px;top:282px;font-size:38px;">Thank you</div>
</section>
<section class="card thanks-inside" style="left:881px;top:0;width:319px;height:412px;">
  <div class="dots" style="left:51px;width:218px;top:74px;"></div>
  <div class="abs script center" style="left:160px;top:106px;font-size:25px;">For being with</div>
  <div class="abs script center" style="left:160px;top:162px;font-size:25px;">me and sharing in</div>
  <div class="abs script center" style="left:160px;top:218px;font-size:25px;">the celebration of this</div>
  <div class="abs script center" style="left:160px;top:274px;font-size:25px;">wonderful occasion.</div>
  <div class="dots" style="left:51px;width:218px;top:338px;"></div>
</section>
<div class="caption" style="left:874px;top:430px;">Thank you card</div>

<!-- Invitation -->
<section class="card invitation" style="left:550px;top:474px;width:319px;height:448px;">
  <div class="abs center" style="left:160px;top:30px;font-family:'Varela Round',sans-serif;font-size:26px;">Celebrating a</div>
  <div class="abs script center" style="left:160px;top:70px;font-size:40px;">Baby on the way</div>
  <div class="dots" style="left:42px;width:238px;top:152px;"></div>
  <div class="abs" style="left:34px;top:168px;font-size:18px;">Join us for a shower honoring:</div>
  <div class="abs" style="left:34px;top:234px;font-size:18px;">Date:</div>
  <div class="abs" style="left:34px;top:266px;font-size:18px;">Time:</div>
  <div class="abs" style="left:34px;top:299px;font-size:18px;">Place:</div>
  <div class="abs" style="left:34px;top:331px;font-size:18px;">Details:</div>
  <div class="abs" style="left:34px;top:364px;font-size:18px;">RSVP to:</div>
  <div class="abs" style="left:34px;top:397px;font-size:18px;">Hosted by:</div>
</section>
<div class="caption" style="left:710px;top:940px;">Invitation</div>

<!-- Diaper raffle ticket -->
<section class="card raffle" style="left:894px;top:474px;width:262px;height:148px;">
  <div class="abs script center" style="left:131px;top:16px;font-size:23px;">Diaper raffle ticket</div>
  <div class="abs center label" style="left:131px;top:65px;">Bring a pack of diapers (any size)</div>
  <div class="abs center label" style="left:131px;top:84px;">for your chance to win a prize!</div>
  <div class="abs label" style="left:17px;top:115px;">Name:</div>
  <div class="rule" style="left:63px;width:181px;top:127px;"></div>
</section>
<div class="caption" style="left:1025px;top:640px;">Diaper raffle ticket</div>

</body>
</html>
```